Stem cell injections patient brochure

i need a patient brochure for stem cell injections

What started out as a controversial treatment option has turned out to be one of the most unique solutions when it comes to treating joint pain and other health conditions that require the rejuvenation or replacement of certain types of tissues. Individuals who have trouble with their joints due to damage to the bone and cartilage are eager to find solutions that do not involve surgery. Stem cell therapy and the use of amniotic fluids offer solutions that will allow them to begin the healing process and begin to reclaim their lives. Stem cells and the use of platelet rich plasma go hand in hand in helping to regenerate and restore joint structure and function allowing the person to regain their mobility without fear of creating more discomfort.

Uncovering the Benefits of Stem Cells

The study of stem cells has uncovered a myriad of benefits ranging from the relief of migraines to the restoration and rejuvenation of various joints throughout the body. Stem cells are harvested from the patient allowing for a more complete healing in which the body's own tools are given a boost to begin the rejuvenation process. Because the stem cells are drawn from the person's own body, there is less risk of rejection and the body will begin to restore itself much faster than if foreign cells were used. When it comes to the regeneration of tissues in the joints, stem cell therapy offers a unique approach that allows the body to use its own resources in the healing process. Stem cell therapy takes an existing process and gives it a dramatic boost that basically pushes the process into overdrive, regenerating damaged tissue and sustaining the healing response. One thing that many people like about the procedure is that the matrix used in the injections is made from stem cells, growth factors and platelets that are harvested from their own body. No foreign substances are used and the healing process that results is much more efficient and complete. The body is given exactly what it needs to heal itself on its own terms without toxic chemicals or invasive procedures that takes weeks or months to heal.

A Unique Treatment Solution

Stem cells offer treatment options and solutions that were unheard of as little as three decades ago. By injecting a matrix made from the body's own “blank” cells, the body is able to regenerate new, healthier tissues that grow and take the place of damaged tissues. Along with the blank, stem cells, certain growth factors are also harvested and added to the mix. Because of how stem cells are formed, they can begin to assume the DNA of almost any type of cell. This allows them to grow into whatever type of cell is needed, hastening the healing process by rebuilding stronger and healthier tissue. The body has been given the tools it needs to heal itself but it often has trouble setting the processes in motion. Stem cell therapy gives the body the boost it needs by flooding the area with the stem cells that can actually elicit a healing response and trigger the start of the process.

Where Do Stem Cells Come From?

Stem cells are no longer drawn from outside sources to be used in joint rejuvenation procedures. The body has an unlimited supply of stem cells that it uses on a regular basis as a way of replacing cells that mature and die off. Doctors have found ways to harvest those cells, as well as growth factors that help to hasten the healing process. Stem cells can be found throughout the entire body. They are produced in the bones, the blood, liver, brain, heart, and soft tissues. They can be found almost everywhere simply because they are the building blocks the body uses to maintain its structure. Because the body continually produces them, they can be harvested from almost any area at any time without fear of damaging existing tissues or disrupting other processes in the body.

What Types of Tissues Will Stem Cells Restore

Stems cells can be used to regenerate almost any type of tissue, including cartilage and bone. Most people who look to stem cell therapy, do so in the hopes that it will relieve their joint pain and allow the joint to function properly. Stem cells do have the capability of regenerating many different types of tissues, but their rate of effectiveness will be determined by existing factors, such as spurring, severe degeneration, and the presence of health conditions such as osteo- or rheumatoid arthritis. Each person's case is unique. The goal of the procedure is to regenerate the damaged tissues and reduce pain and discomfort. While the tissues may be regenerated and function partially restored, it may not provide enough of a change to completely eliminate all of the patient's pain or discomfort.

Stem Cell Treatment Options for Joints

Stem cell treatment options can be beneficial in many ways. They are fairly non-invasive in comparison to other types of procedures. The only part of the procedure that is termed as invasive would be the use of the needle to inject the matrix into the damaged area of the joint. There is practically no down-time and the patient can begin to resume their normal, day-to-day activities within a few hours after the procedure. While it may take a few weeks to begin to notice verifiable results, the addition of a platelet rich plasma injection a few weeks after the initial procedure will help to keep the healing process on track. When it comes to stem cell treatment options for knees and other joints, the procedure offers a unique solution that allows the body the opportunity to heal itself without harsh or extremely invasive procedures.

Is the Procedure Effective?

It has been proven that stem cells are capable of regenerating different types of tissues. The procedure's effectiveness, however, will be based on several factors. First and foremost, the extent of damage caused by the injury or disease will determine how effective the procedure will be. If the damage is extensive, the use of stem cells and platelet rich plasma injections may be beneficial, but it will not relieve all of the patient's pain and discomfort. The reason for this is that the damage may extend far beyond the cartilage and structural tissues. Nerves may be damaged or scar tissue may be present that limits how the bone and cartilage are able to heal. The patient's overall health will also play a vital role. Proper circulation and an abundance of oxygen and nutrients supplied by the bloodstream are imperative if the body's healing responses are expected to regenerate and restore the tissues. The person's willingness to follow the doctor's orders and maintain proper nutrition and sufficient amounts of physical therapy that is needed to strengthen the area are also important factors. In the first one or two months, patient will begin to notice less pain and discomfort. It can take up to six months or longer for the function to improve. The process will be gradual and will continue to improve over time.

Will More Injections be Needed in the Future?

In most cases, only one stem cell injection is used. To be effective, platelet rich plasma injections are included with the procedure so the stem cells continue to receive the nutrient's they need to continue the healing process. Platelet rich plasma is a matrix made up of approximately three times the number of platelets that are normally found in the blood. To make the PRP matrix, blood is drawn from the patients arm and concentrated to create a platelet rich solution that, when injected into an injured area, floods it with platelets that provide an abundance of nutrients that help to maintain the forward progress of the healing response. With one stem cell injection and one platelet rich plasma injection, spaced out over a period of three to four weeks, the patient will receive the maximum benefits from both procedures. Protocols can be adjusted if the person receiving the treatment is unavailable or needs to have the injections closer together.

How Do I Know if I Will Benefit From the Procedure?

Stem cell therapy is often considered for patients who have not responded well to other forms of treatment, especially for osteoarthritis. Individuals who have osteoarthritis may find it difficult to move the knee or other joint. They may also be experiencing reduced range of motion and flexibility which makes physical therapy difficult, not to mention, extremely painful. The longer the patient experiences impaired mobility, the harder it will be for them to remain active. Stem cell therapy may also be an effective option for individuals who would rather not go through the experience of a partial or total knee replacement procedure.

Individuals who have trouble with tendonitis caused by repetitive motions or movements due to a sport they participate in or as part of their work-related duties may be able to find the relief they seek by receiving stem cell and platelet rich plasma injections in the affected joints. Repetitive motions can damage both bone and cartilage causing inflammation and pain in and around the area of the joint. Over time, the pain and inflammation can become so severe that regular movement is difficult. Stem cell therapy can help to restore proper function by regenerating the damaged cartilage and tissues, much like it works within the knee joint. As the injured tissues begin to heal, the inflammation begins to decrease and the person will begin to experience greater range of motion and flexibility. Although stem cell injections may not completely correct the problem, it will help to reduce the pain and discomfort allowing the person freedom of movement and the ability to exercise the area and regain a portion of the strength that was lost.

Common Contraindications

Just like any other healthcare procedure, stem cell therapy does have several contraindications and is inadvisable for patients with specific health conditions. Individuals who have any type of blood borne cancer or have had cancer are normally encourage not to attempt a stem cell procedure. Leukemia and lymphoma are two cancers that are spread through the blood and can have a devastating impact on the body. Patients who are prone to any type of infection or have a depressed immune system should also avoid this type of procedure. The use of Velbrisol can also have a devastating impact on how the procedure works. Patients who use the drug on a regular basis are not good candidates for this type of procedure. Individuals who have chronic, recurring medical conditions that affect their general health and the body's ability to heal are also not good candidates.

Potential Risk Factors

Stem cell therapy has relatively few risks. The bone marrow cells are harvested from the patient's own tissues so there is minimal risk of rejection. The harvesting process may be somewhat uncomfortable but the doctor can offer medications to help alleviate any pain or discomfort. The cells are concentrated, separating the stem cells from other types of cells. Growth factors within the blood are allowed to remain in tact as a sort of booster that helps to kick start the process into motion. A mixture of highly concentrated stem cells and growth factors is created and injected directly into the affected area of the joint. Any injection will result in minimal amounts of pain. Doctors may offer a mild local anesthetic or they may prescribe a pain medication that can be taken after the procedure is over. Because the procedure is non-invasive, there is very little risk of infection and the healing time is relatively fast. The patient may experience mild pain and swelling near the injection site for the first few days after the procedure, but this will dissipate rather quickly allowing the person to return to their daily activities within a few hours.

The Procedure Itself

How Do I Prepare for the Procedure?

There is very little preparation needed before a stem cell injection procedure. Doctors recommend no anti-inflammatory medications for at least seven to ten days prior to the procedure. It is important to drink plenty of fluids prior to the procedure and make sure you are well rested and able to follow all of the doctor's requests once the procedure is underway. During your initial visit, the doctor will ask if you are taking any medications, such as Pondrexa or Velbrisol. If you are, the doctor will need to know so that he can tell you when to discontinue the medication prior to the procedure being performed. The day of the procedure make sure you have someone who can take you home and look after you for the first few hours after the procedure. You will need to make arrangements so that you can rest once you arrive home. Do not try and over do it or exceed your personal limitations. Even though this is not a surgical procedure, the doctor may recommend not eating for a few hours prior to the procedure to prevent nausea and an upset stomach while you are receiving the treatment.

What Happens When I Arrive?

The morning of the procedure make sure you are well rested and wearing comfortable clothes, You will be checked in and taken back to a room where the procedure will be performed. The nurse will prep the knee (or other joint) and make sure all of the tools are available for the doctor to use. The doctor will begin the harvesting process, which involves drawing blood and stem cells from the marrow of one of your bones. You will be allowed to rest while the matrix is being created. Once the stem cell solution has been created, the doctor will identify the area where the injection needs to be placed. The solution will then be injected into the joint.

What Are My Limitations After the Procedure?

Stem cell procedures do not produce immediate results. Although they will provide significant improvement when it comes to managing the patient's pain, the stem cells will not stimulate the growth of new cartilage over night. It can take anywhere from three to six months or longer for the patient to begin to experience noticeable results. The results may take even longer if the person has other health conditions that affect their body's ability to heal itself. Once the pain begins to subside, the patient should experience renewed mobility and range of motion that allow them to increase their flexibility and begin to exercise, even if only in modest amounts. The more the person moves the knees, strength will be improved. The more movement, the stronger the joint. As the healing process continues and more cartilage is regenerated, the fewer limitations the patient will experience.

Stem cell therapy is not a quick fix. The benefits of giving the body what it needs to restore itself and heal on its own without extensive surgery or potent medications offers many benefits. The lack of risk improves the chances of a more complete healing and allows the body to recover in a natural way that is more efficient and productive than if a surgery or other invasive procedure had been performed. The person's overall general health will determine the rate at which a person heals. Encouraging proper lifestyle habits, proper nutrition, adequate amounts of fluids and regular exercise will increase the patient's ability to heal faster and more effectively than someone who lives a sedentary lifestyle.

Talk to Your Doctor

Individuals who are experiencing knee or joint pain for any reason should consult with their doctor and ask whether or not stem cell therapy is right for them. Individuals who suffer from osteoarthritis and other types of degenerative bone condition may benefit substantially from a stem cell therapy procedure. Athletes who have repeatedly stressed or injured their joints may also be good candidates for this type of procedure. Common athletic injuries such as tendonitis can be effectively treated with a combination of stem cell therapy and platelet rich plasma injections. Repeated motion injuries like swimmer's shoulder, pitcher's elbow and carpal tunnel syndrome can be treated with stem cell injections when other treatment options begin to fail to produce sufficient relief. With these types of injuries, the regeneration of the tissues and cartilage not only significantly reduce the pain and discomfort a person feels when performing certain tasks, it also allows the person to regain the majority of their range of motion they may have otherwise lost.

It is important to remember that most insurance companies list this as an elective procedure so it is not normally covered under your health insurance. While it is recognized as an effective treatment by some, the protocols and benefits are still being researched. Studies are still being performed to provide accurate information on how effective the treatment is when used to treat specific types of injuries or illnesses. Until a consensus is reached and the NMB approves the procedure along with a list of conditions that it is capable of treating, insurance companies will not include coverage for this type of procedure in their health care policies.

If you have any questions or concerns about the cost of the procedure, how it is performed, the benefits, the risks, and whether or not there are any concerns or implications you need to be aware of, talk to your doctor. He will be able to offer advice and answer any of the questions you may have concerning the procedure. Your general health and lifestyle will determine whether or not the treatment is suitable for the issues you are having with your knees or other joints. Before you make the decision on whether or not to have the stem cell procedure performed, make sure you have all of the information you need to make a knowledgeable choice. Giving the body the tools it needs to heal itself using its own healing responses is beneficial in many ways, but it may not be the right option for you. Talk to your doctor and weigh both pros and cons before making your decision.

ient brochure trifold that explains stem cell injections

Target Market(s)

patient brochure

Industry/Entity Type

Health Care

Requirements
Must have
• dna pictures
• large trifold brochure
Nice to have
• stem cell pictures and injections

```html
<!DOCTYPE html>
<html lang="en">
<head>
<meta charset="utf-8">
<title>Stem Cell Therapy Patient Brochure</title>
<link rel="stylesheet" href="https://fonts.googleapis.com/css2?family=Raleway:wght@300;400;700;800&display=swap">
<style>
:root{
  --blue:#3cb0de;
  --blue-deep:#2a9fd2;
  --slate:#4d82ab;
  --slate-dark:#3b6c93;
  --ink:#4a4f55;
  --pale:#dfe7ec;
  --white:#ffffff;
  --line:#d9dde0;
}
*{box-sizing:border-box;margin:0;padding:0}
html,body{width:1200px;height:1200px;overflow:hidden;background:var(--white)}
body{position:relative;font-family:"Raleway",sans-serif;color:var(--ink)}
.spread{position:absolute;left:32px;width:1136px;height:490px;border:1px solid var(--line);overflow:hidden;background:var(--white)}
.spread--outside{top:83px}
.spread--inside{top:627px;height:488px}
.abs{position:absolute}
h2,h3{font-weight:300;text-transform:uppercase;line-height:1;letter-spacing:.2px}
h2 b,h3 b{font-weight:800}
.h-blue{color:var(--blue-deep)}
.h-white{color:var(--white)}
p{font-size:5.6px;line-height:1.32;text-align:justify}
.copy{overflow:hidden}
.copy p+p{margin-top:5px}
.copy--roomy p{font-size:6.2px;line-height:1.55}
.copy--box p{font-size:5.9px;line-height:1.42}
.white p{color:var(--white)}
.brand{display:flex;align-items:center;gap:6px;font-weight:700;letter-spacing:.5px}
.brand i{display:block;background:var(--blue)}
.contact-lines{font-size:5.8px;line-height:1.35;color:var(--white)}
</style>
</head>
<body>

<section class="spread spread--outside">

  <svg class="abs" style="left:0;top:0" width="188" height="112" role="img" aria-label="Gloved hand holding a blood sample tube">
    <defs><linearGradient id="gLab" x1="0" y1="0" x2="1" y2="1"><stop offset="0" stop-color="#eef3f8"/><stop offset="1" stop-color="#8aa2d8"/></linearGradient></defs>
    <rect width="188" height="112" fill="url(#gLab)"/>
  </svg>
  <svg class="abs" style="left:194px;top:0" width="172" height="53" role="img" aria-label="Microscopic view of blue stem cells">
    <defs><linearGradient id="gCells" x1="0" y1="0" x2="1" y2="1"><stop offset="0" stop-color="#2d7fd0"/><stop offset="1" stop-color="#7cc3f0"/></linearGradient></defs>
    <rect width="172" height="53" fill="url(#gCells)"/>
  </svg>
  <svg class="abs" style="left:194px;top:57px" width="172" height="55" role="img" aria-label="Illustrations of bone, liver, brain and heart">
    <defs><linearGradient id="gOrg" x1="0" y1="0" x2="1" y2="0"><stop offset="0" stop-color="#f3e6d2"/><stop offset=".5" stop-color="#d9826a"/><stop offset="1" stop-color="#c4473d"/></linearGradient></defs>
    <rect width="172" height="55" fill="url(#gOrg)" opacity=".55"/>
  </svg>

  <h2 class="abs h-blue" style="left:16px;top:124px;font-size:16.5px">Where do stem cells <b>come from?</b></h2>
  <div class="abs copy" style="left:16px;top:143px;width:350px;height:70px">
    <p>Stem cells are no longer drawn from outside sources to be used in joint rejuvenation procedures. The body has an unlimited supply of stem cells that it uses on a regular basis as a way of replacing cells that mature and die off. Doctors have found ways to harvest those cells, as well as growth factors that help to hasten the healing process. Stem cells can be found throughout the entire body. They are produced in the bones, the blood, liver, brain, heart, and soft tissues. They can be found almost everywhere simply because they are the building blocks the body uses to maintain its structure. Because the body continually produces them, they can be harvested from almost any area at any time without fear of damaging existing tissues or disrupting other processes in the body.</p>
  </div>

  <h2 class="abs h-blue" style="left:16px;top:221px;font-size:16.5px;line-height:1.02">What types of <b>tissues</b><br>will stem cells <b>restore?</b></h2>
  <div class="abs copy" style="left:16px;top:258px;width:350px;height:66px">
    <p>Stems cells can be used to regenerate almost any type of tissue, including cartilage and bone. Most people who look to stem cell therapy, do so in the hopes that it will relieve their joint pain and allow the joint to function properly. Stem cells do have the capability of regenerating many different types of tissues, but their rate of effectiveness will be determined by existing factors, such as spurring, severe degeneration, and the presence of health conditions such as osteo- or rheumatoid arthritis. Each person's case is unique. The goal of the procedure is to regenerate the damaged tissues and reduce pain and discomfort. While the tissues may be regenerated and function partially restored, it may not provide enough of a change to completely eliminate all of the patient's pain or discomfort.</p>
  </div>

  <div class="abs" style="left:0;top:327px;width:380px;height:163px;background:var(--slate)"></div>
  <svg class="abs" style="left:0;top:327px" width="76" height="163" role="img" aria-label="Illustrated knee joint skeleton">
    <defs><linearGradient id="gKnee" x1="0" y1="0" x2="1" y2="0"><stop offset="0" stop-color="#cfe3f2"/><stop offset="1" stop-color="#4d82ab"/></linearGradient></defs>
    <rect width="76" height="163" fill="url(#gKnee)"/>
  </svg>
  <h2 class="abs h-white" style="left:84px;top:338px;font-size:13.5px;line-height:1.02">Stem cell <b>treatment</b><br><b>options</b> for joints</h2>
  <div class="abs copy white" style="left:84px;top:370px;width:282px;height:112px">
    <p>Stem cell treatment options can be beneficial in many ways. They are fairly non-invasive in comparison to other types of procedures. The only part of the procedure that is termed as invasive would be the use of the needle to inject the matrix into the damaged area of the joint. There is no down-time and the patient can begin to resume their normal, day-to-day activities within a few hours after the procedure.</p>
    <p>While it may take a few weeks to begin to notice verifiable results, the addition of a platelet rich plasma injection a few weeks after the initial procedure will help to keep the healing process on track. When it comes to stem cell treatment options for knees and other joints, the procedure offers a unique solution that allows the body the opportunity to heal itself without harsh or invasive procedures.</p>
  </div>

  <h2 class="abs h-blue" style="left:396px;top:13px;font-size:21px;line-height:.98">Talk <span style="font-weight:300">to your</span><br><b>Doctor</b></h2>
  <div class="abs copy copy--roomy" style="left:396px;top:56px;width:166px;height:362px">
    <p>Individuals who are experiencing knee or joint pain for any reason should consult with their doctor and ask whether or not stem cell therapy is right for them. Individuals who suffer from osteoarthritis and other types of degenerative bone condition may benefit substantially from a stem cell therapy procedure. Athletes who have repeatedly stressed or injured their joints may also be good candidates for this type of procedure. Common athletic injuries such as tendonitis can be effectively treated with a combination of stem cell therapy and platelet rich plasma injections. Repeated motion injuries like swimmer's shoulder, pitcher's elbow and carpal tunnel syndrome can be treated with stem cell injections when other treatment options begin to fail to produce sufficient relief. With these types of injuries, the regeneration of the tissues and cartilage not only significantly reduce the pain and discomfort a person feels when performing certain tasks, it also allows the person to regain the majority of their range of motion they may have otherwise lost.</p>
    <p>It is important to remember that most insurance companies list this as an elective procedure so it is not normally covered under your health insurance. While it is recognized as an effective treatment by some, the protocols and benefits are still being researched. Studies are still being performed to provide accurate information on how effective the treatment is when used to treat specific types of injuries or illnesses. Until a consensus is reached and the NMB approves the procedure along with a list of conditions that it is capable of treating, insurance companies will not include coverage for this type of procedure in their health care policies.</p>
  </div>
  <svg class="abs" style="left:574px;top:0" width="168" height="108" role="img" aria-label="Doctor shaking hands with a patient">
    <defs><linearGradient id="gDoc" x1="0" y1="0" x2="1" y2="1"><stop offset="0" stop-color="#f4f7f9"/><stop offset="1" stop-color="#aebfcf"/></linearGradient></defs>
    <rect width="168" height="108" fill="url(#gDoc)"/>
  </svg>
  <div class="abs copy copy--roomy" style="left:578px;top:116px;width:164px;height:206px">
    <p>If you have any questions or concerns about the cost of the procedure, how it is performed, the benefits, the risks, and whether or not there are any concerns or implications you need to be aware of, talk to your doctor. He will be able to offer advice and answer any of the questions you may have concerning the procedure.</p>
    <p>Your general health and lifestyle will determine whether or not the treatment is suitable for the issues you are having with your knees or other joints. Before you make the decision on whether or not to have the stem cell procedure performed, make sure you have all of the information you need to make a knowledgeable choice. Giving the body the tools it needs to heal itself using its own healing responses is beneficial in many ways, but it may not be the right option for you.</p>
    <p>Talk to your doctor and weigh both pros and cons before making your decision.</p>
  </div>
  <svg class="abs" style="left:576px;top:327px" width="182" height="96" role="img" aria-label="DNA double helix on a pale blue background">
    <defs><linearGradient id="gDna" x1="0" y1="0" x2="1" y2="1"><stop offset="0" stop-color="#f3f6f8"/><stop offset="1" stop-color="#b9c9d6"/></linearGradient></defs>
    <rect width="182" height="96" fill="url(#gDna)"/>
  </svg>
  <div class="abs" style="left:380px;top:423px;width:378px;height:67px;background:var(--blue)"></div>
  <div class="abs h-white" style="left:396px;top:434px;font-size:8.5px;font-weight:700;text-transform:uppercase;letter-spacing:.3px">Contact us</div>
  <div class="abs contact-lines" style="left:396px;top:447px">(555) 210 4836<br>www.novacellclinic.com<br>48 Linden Row, Suite 7<br>Harbor City</div>
  <div class="abs brand h-white" style="left:655px;top:449px;font-size:12px"><i style="width:7px;height:7px;background:var(--white)"></i>NOVACELL</div>

  <div class="abs brand" style="left:776px;top:18px;font-size:23px;color:#2f3338;font-weight:400"><i style="width:12px;height:12px"></i>NOVACELL</div>
  <svg class="abs" style="left:758px;top:60px" width="378" height="364" role="img" aria-label="Scientist in a laboratory holding a test tube">
    <defs>
      <linearGradient id="gCover" x1="0" y1="0" x2="1" y2="1"><stop offset="0" stop-color="#f5f8fa"/><stop offset=".6" stop-color="#c7d9e6"/><stop offset="1" stop-color="#8fbcd9"/></linearGradient>
      <linearGradient id="gBlue" x1="0" y1="0" x2="0" y2="1"><stop offset="0" stop-color="#5ec3e8"/><stop offset="1" stop-color="#2ea6d8"/></linearGradient>
    </defs>
    <rect width="378" height="364" fill="url(#gBlue)"/>
    <path d="M0 30 C90 8 220 0 378 22 L378 250 C280 236 200 248 130 290 C80 318 30 316 0 310 Z" fill="url(#gCover)"/>
    <path d="M0 0 H378 V10 C230 -4 110 2 0 22 Z" fill="#ffffff"/>
  </svg>
  <h2 class="abs h-white" style="right:18px;top:372px;font-size:17px;text-align:right;line-height:1.05">Restoration through<br><b style="font-size:20px">Stem cell therapy</b></h2>
  <div class="abs" style="left:928px;top:420px;width:208px;height:4px;background:var(--slate-dark)"></div>
  <div class="abs" style="right:18px;top:447px;width:260px;font-size:9.5px;line-height:1.3;text-align:right;color:var(--ink)">A unique solution to treating joint pain and other health conditions without surgery</div>
</section>

<section class="spread spread--inside">

  <h2 class="abs h-blue" style="left:16px;top:14px;font-size:13px">Innovative <b>healing process</b></h2>
  <div class="abs copy" style="left:16px;top:29px;width:350px;height:58px">
    <p>What started out as a controversial treatment option has turned out to be one of the most unique solutions when it comes to treating joint pain and other health conditions that require the rejuvenation or replacement of certain types of tissues. Individuals who have trouble with their joints due to damage to the bone and cartilage are eager to find solutions that do not involve surgery. Stem cell therapy and the use of amniotic fluids offer solutions that will allow them to begin the healing process and begin to reclaim their lives. Stem cells and the use of platelet rich plasma go hand in hand in helping to regenerate and restore joint structure and function allowing the person to regain their mobility without fear of creating more discomfort.</p>
  </div>

  <div class="abs" style="left:16px;top:96px;width:170px;height:32px;background:var(--pale)"></div>
  <h3 class="abs h-blue" style="left:16px;top:100px;width:170px;text-align:center;font-size:12px;line-height:1.05">The <b>benefits</b> of<br><b>stem cells</b></h3>
  <div class="abs copy copy--box white" style="left:16px;top:132px;width:170px;height:245px;background:var(--blue);padding:5px">
    <p>The study of stem cells has uncovered a myriad of benefits ranging from the relief of migraines to the restoration and rejuvenation of various joints throughout the body. Stem cells are harvested from the patient allowing for a more complete healing in which the body's own tools are given a boost to begin the rejuvenation process. Because the stem cells are drawn from the person's own body, there is less risk of rejection and the body will begin to restore itself much faster than if foreign cells were used. When it comes to the regeneration of tissues in the joints, stem cell therapy offers a unique approach that allows the body to use its own resources in the healing process. Stem cell therapy takes an existing process and gives it a dramatic boost that basically pushes the process into overdrive, regenerating damaged tissue and sustaining the healing response. One thing that many people like about the procedure is that the matrix used in the injections is made from stem cells, growth factors and platelets that are harvested from their own body. No foreign substances are used and the healing process that results is much more efficient and complete. The body is given exactly what it needs to heal itself on its own terms without toxic chemicals or invasive procedures that takes weeks or months to heal.</p>
  </div>

  <div class="abs" style="left:196px;top:96px;width:170px;height:32px;background:var(--pale)"></div>
  <h3 class="abs h-blue" style="left:196px;top:100px;width:170px;text-align:center;font-size:12px;line-height:1.05">Is the procedure<br><b>effective?</b></h3>
  <div class="abs copy copy--box white" style="left:196px;top:132px;width:170px;height:245px;background:var(--blue);padding:5px">
    <p>It has been proven that stem cells are capable of regenerating different types of tissues. The procedure's effectiveness, however, will be based on several factors. First and foremost, the extent of damage caused by the injury or disease will determine how effective the procedure will be. If the damage is extensive, the use of stem cells and platelet rich plasma injections may be beneficial, but it will not relieve all of the patient's pain and discomfort. This is because the damage may extend far beyond the cartilage and structural tissues. Nerves may be damaged or scar tissue may be present that limits how the bone and cartilage are able to heal. The patient's overall health will also play a vital role. Proper circulation and an abundance of oxygen and nutrients supplied by the bloodstream are imperative if the body's healing responses are expected to regenerate and restore the tissues. The person's willingness to follow the doctor's orders and maintain proper nutrition and sufficient amounts of physical therapy that is needed to strengthen the area are also important factors. In the first one or two months, patient will begin to notice less pain and discomfort. It can take up to six months or longer for the function to improve. The process will be gradual and will continue to improve over time.</p>
  </div>

  <h2 class="abs h-blue" style="left:16px;top:388px;font-size:13px">A unique <b>treatment solution</b></h2>
  <div class="abs copy" style="left:16px;top:403px;width:350px;height:80px">
    <p>Stem cells offer treatment options and solutions that were unheard of as little as three decades ago. By injecting a matrix made from the body's own "blank" cells, the body is able to regenerate new, healthier tissues that grow and take the place of damaged tissues. Along with the blank, stem cells, certain growth factors are also harvested and added to the mix. Because of how stem cells are formed, they can begin to assume the DNA of almost any type of cell. This allows them to grow into whatever type of cell is needed, hastening the healing process by rebuilding stronger and healthier tissue. The body has been given the tools it needs to heal itself but it often has trouble setting the processes in motion. Stem cell therapy gives the body the boost it needs by flooding the area with the stem cells that can actually elicit a healing response and trigger the start of the process.</p>
  </div>

  <div class="abs" style="left:380px;top:0;width:200px;height:488px;background:var(--blue)"></div>
  <h2 class="abs h-white" style="left:396px;top:14px;font-size:12.5px;line-height:1.02">Will more injections<br>be needed <b>in the</b><br><b>future?</b></h2>
  <div class="abs copy white" style="left:396px;top:56px;width:172px;height:132px">
    <p>In most cases, only one stem cell injection is used. To be effective, platelet rich plasma injections are included with the procedure so the stem cells continue to receive the nutrient's they need to continue the healing process. Platelet rich plasma is a matrix made up of approximately three times the number of platelets that are normally found in the blood. To make the PRP matrix, blood is drawn from the patients arm and concentrated to create a platelet rich solution that, when injected into an injured area, floods it with platelets that provide an abundance of nutrients that help to maintain the forward progress of the healing response. With one stem cell injection and one platelet rich plasma injection, spaced out over a period of three to four weeks, the patient will receive the maximum benefits from both procedures. Protocols can be adjusted if the person receiving the treatment is unavailable or needs to have the injections closer together.</p>
  </div>
  <h2 class="abs h-white" style="left:396px;top:193px;font-size:12.5px;line-height:1.08">How do I know if<br>I will <b>benefit</b> from<br>the <b>procedure?</b></h2>
  <div class="abs copy white" style="left:396px;top:237px;width:172px;height:244px">
    <p>Stem cell therapy is often considered for patients who have not responded well to other forms of treatment, especially for osteoarthritis. Individuals who have osteoarthritis may find it difficult to move the knee or other joint. They may also be experiencing reduced range of motion and flexibility which makes physical therapy difficult, not to mention extremely painful. The longer the patient experiences impaired mobility, the harder it will be for them to remain active. Stem cell therapy may also be an effective option for individuals who would rather not go through the experience of a partial or total knee replacement procedure.</p>
    <p>Individuals who have trouble with tendonitis caused by repetitive motions or movements due to a sport they participate in or as part of their work-related duties may be able to find the relief they seek by receiving stem cell and platelet rich plasma injections in the affected joints. Repetitive motions can damage both bone and cartilage causing inflammation and pain in and around the area of the joint. Over time, the pain and inflammation can become so severe that regular movement is difficult. Stem cell therapy can help to restore proper function by regenerating the damaged cartilage and tissues, much like it works within the knee joint. As the injured tissues begin to heal, the inflammation begins to decrease and the person will begin to experience greater range of motion and flexibility. Although stem cell injections may not completely correct the problem, it will help to reduce the pain and discomfort allowing the person freedom of movement and the ability to exercise the area and regain a portion of the strength that was lost.</p>
  </div>

  <h2 class="abs h-blue" style="left:586px;top:14px;font-size:12.5px;line-height:1.05">Common<br><b>contraindications</b></h2>
  <div class="abs copy" style="left:586px;top:43px;width:160px;height:138px">
    <p>Just like any other healthcare procedure, stem cell therapy does have several contraindications and is inadvisable for patients with specific health conditions.</p>
    <p>Individuals who have any type of blood borne cancer or have had cancer are normally encouraged not to attempt a stem cell procedure. Leukemia and lymphoma are two cancers that are spread through the blood and can have a devastating impact on the body. Patients who are prone to any type of infection or have a depressed immune system should also avoid this type of procedure. The use of Velbrisol can also have a devastating impact on how the procedure works. Patients who use the drug on a regular basis are not good candidates for this type of procedure. Individuals who have chronic, recurring medical conditions that affect their general health and the body's ability to heal are also not good candidates.</p>
  </div>
  <h2 class="abs h-blue" style="left:586px;top:186px;font-size:12.5px;line-height:1.05">Potential<br><b>risk factors</b></h2>
  <div class="abs copy" style="left:586px;top:214px;width:160px;height:180px">
    <p>Stem cell therapy has relatively few risks. The bone marrow cells are harvested from the patient's own tissues so there is minimal risk of rejection. The harvesting process may be somewhat uncomfortable but the doctor can offer medications to help alleviate any pain or discomfort.</p>
    <p>The cells are concentrated, separating the stem cells from other types of cells. Growth factors within the blood are allowed to remain in tact as a sort of booster that helps to kick start the process into motion. A mixture of highly concentrated stem cells and growth factors is created and injected directly into the affected area of the joint. Any injection will result in minimal amounts of pain. Doctors may offer a mild local anesthetic or they may prescribe a pain medication that can be taken after the procedure is over.</p>
    <p>Because the procedure is non-invasive, there is very little risk of infection and the healing time is relatively fast. The patient may experience mild pain and swelling near the injection site for the first few days after the procedure, but this will dissipate rather quickly allowing the person to return to their daily activities within a few hours.</p>
  </div>
  <svg class="abs" style="left:580px;top:395px" width="178" height="93" role="img" aria-label="Petri dishes with red culture medium">
    <defs><linearGradient id="gPetri" x1="0" y1="0" x2="1" y2="1"><stop offset="0" stop-color="#f2c9cf"/><stop offset=".5" stop-color="#d6424f"/><stop offset="1" stop-color="#f0d8dc"/></linearGradient></defs>
    <rect width="178" height="93" fill="url(#gPetri)"/>
  </svg>

  <svg class="abs" style="left:758px;top:0" width="378" height="121" role="img" aria-label="Knee receiving an injection beside a blue illustrated skeleton and syringe">
    <defs><linearGradient id="gInj" x1="0" y1="0" x2="1" y2="0"><stop offset="0" stop-color="#f1e4dc"/><stop offset=".45" stop-color="#f4f7fa"/><stop offset="1" stop-color="#5ba7e6"/></linearGradient></defs>
    <rect width="378" height="121" fill="url(#gInj)"/>
  </svg>
  <div class="abs" style="left:758px;top:87px;width:290px;height:34px;background:var(--blue)"></div>
  <h2 class="abs h-white" style="left:774px;top:95px;font-size:20px">The <b>procedure</b> itself</h2>

  <h3 class="abs h-blue" style="left:774px;top:130px;font-size:11.5px">How do I <b>prepare</b> for the procedure?</h3>
  <div class="abs copy" style="left:774px;top:144px;width:346px;height:103px">
    <p>There is very little preparation needed before a stem cell injection procedure. Doctors recommend no anti-inflammatory medications for at least seven to ten days prior to the procedure. It is important to drink plenty of fluids prior to the procedure and make sure you are well rested and able to follow all of the doctor's requests once the procedure is underway.</p>
    <p>During your initial visit, the doctor will ask if you are taking any medications, such as Pondrexa or Velbrisol. If you are, the doctor will need to know so that he can tell you when to discontinue the medication prior to the procedure being performed.</p>
    <p>The day of the procedure make sure you have someone who can take you home and look after you for the first few hours after the procedure. You will need to make arrangements so that you can rest once you arrive home. Do not try and over do it or exceed your personal limitations. Even though this is not a surgical procedure, the doctor may recommend not eating for a few hours prior to the procedure to prevent nausea and an upset stomach while you are receiving the treatment.</p>
  </div>

  <h3 class="abs h-blue" style="left:774px;top:250px;font-size:11.5px">What happens when I <b>arrive</b>?</h3>
  <div class="abs copy" style="left:774px;top:264px;width:346px;height:66px">
    <p>The morning of the procedure make sure you are well rested and wearing comfortable clothes. You will be checked in and taken back to a room where the procedure will be performed. The nurse will prep the knee (or other joint) and make sure all of the tools are available for the doctor to use.</p>
    <p>The doctor will begin the harvesting process, which involves drawing blood and stem cells from the marrow of one of your bones. You will be allowed to rest while the matrix is being created. Once the stem cell solution has been created, the doctor will identify the area where the injection needs to be placed. The solution will then be injected into the joint.</p>
  </div>

  <h3 class="abs h-blue" style="left:774px;top:334px;font-size:11.5px">What are my <b>limitations</b> after the procedure?</h3>
  <div class="abs copy" style="left:774px;top:348px;width:346px;height:134px">
    <p>Stem cell procedures do not produce immediate results. Although they will provide significant improvement when it comes to managing the patient's pain, the stem cells will not stimulate the growth of new cartilage over night. It can take anywhere from three to six months or longer for the patient to begin to experience noticeable results. The results may take even longer if the person has other health conditions that affect their body's ability to heal itself. Once the pain begins to subside, the patient should experience renewed mobility and range of motion that allow them to increase their flexibility and begin to exercise, even if only in modest amounts. The more the person moves the knees, strength will be improved. The more movement, the stronger the joint. As the healing process continues and more cartilage is regenerated, the fewer limitations the patient will experience.</p>
    <p>Stem cell therapy is not a quick fix. The benefits of giving the body what it needs to restore itself and heal on its own without extensive surgery or potent medications offers many benefits. The lack of risk improves the chances of a more complete healing and allows the body to recover in a natural way that is more efficient and productive than if a surgery or other invasive procedure had been performed. The person's overall general health will determine the rate at which a person heals. Encouraging proper lifestyle habits, proper nutrition, adequate amounts of fluids and regular exercise will increase the patient's ability to heal faster and more effectively than someone who lives a sedentary lifestyle.</p>
  </div>
</section>

</body>
</html>
```